Attractive Wall Posters wanted

We are designing posters for our outdoor wall to represent our brands.

(Portrait Layout: Measurements - Height 128cm, Width 108cm).

More information for each brand can be found on the website listed in the ppt attached.

Requirements
Must have
• The information included in PPT, the logo, the website and the short description
Nice to have
• Consistency across all posters
Should not have
• too cluttered designs

```html
<!DOCTYPE html>
<html lang="en">
<head>
<meta charset="utf-8">
<title>Lumen Foundation – Social Enterprise Poster</title>
<link href="https://fonts.googleapis.com/css2?family=Archivo:wght@300;800&family=Oswald:wght@600&display=swap" rel="stylesheet">
<style>
  :root {
    --backdrop: #c9cacc;
    --paper: #f1f1f1;
    --paper-edge: #fafafa;
    --brand-green: #8fa82a;
    --ink: #1e1e1e;
    --band-dark: #1b1b1b;
    --white: #ffffff;
    --art-tone: #dcdcdc;
  }
  html, body {
    margin: 0;
    padding: 0;
    width: 1200px;
    height: 1200px;
    overflow: hidden;
    background: var(--backdrop);
  }
  .poster {
    position: absolute;
    left: 127px;
    top: 40px;
    width: 945px;
    height: 1120px;
    background: radial-gradient(ellipse at 50% 40%, #f7f7f7 0%, var(--paper) 60%, #e8e8e8 100%);
    overflow: hidden;
  }
  .poster__frame {
    position: absolute;
    inset: 14px;
    border: 2px solid var(--paper-edge);
    pointer-events: none;
  }
  .brand {
    position: absolute;
    left: 0;
    right: 0;
    top: 80px;
    display: flex;
    flex-direction: column;
    align-items: center;
  }
  .brand__mark {
    width: 200px;
    height: 200px;
  }
  .brand__name {
    margin-top: 30px;
    font-family: "Oswald", sans-serif;
    font-weight: 600;
    font-size: 54px;
    line-height: 1;
    color: var(--brand-green);
    letter-spacing: -0.5px;
  }
  .backdrop-art {
    position: absolute;
    left: 119px;
    top: 414px;
    width: 653px;
    height: 586px;
    background: radial-gradient(ellipse at 50% 65%, var(--art-tone) 0%, rgba(220,220,220,0.5) 45%, rgba(240,240,240,0) 75%);
  }
  .headline {
    position: absolute;
    left: 0;
    right: 0;
    top: 478px;
    text-align: center;
    font-family: "Archivo", sans-serif;
  }
  .headline__main {
    display: block;
    font-weight: 800;
    font-size: 148px;
    line-height: 1;
    color: var(--brand-green);
    letter-spacing: -3px;
  }
  .headline__sub {
    display: block;
    margin-top: 2px;
    font-weight: 300;
    font-size: 92px;
    line-height: 1;
    color: var(--ink);
    letter-spacing: -1px;
  }
  .footer-band {
    position: absolute;
    left: 0;
    top: 990px;
    width: 945px;
    height: 90px;
  }
  .footer-band__url {
    position: absolute;
    left: 0;
    right: 0;
    top: 1012px;
    text-align: center;
    font-family: "Oswald", sans-serif;
    font-weight: 600;
    font-size: 40px;
    line-height: 50px;
    color: var(--white);
    padding-left: 70px;
  }
</style>
</head>
<body>
  <main class="poster">
    <div class="poster__frame"></div>

    <div class="backdrop-art" role="img" aria-label="Faint dotted world map with raised open hands, symbolising community support"></div>

    <header class="brand">
      <svg class="brand__mark" viewBox="0 0 200 200" aria-hidden="true">
        <circle cx="100" cy="100" r="90" fill="none" stroke="var(--brand-green)" stroke-width="6"/>
      </svg>
      <div class="brand__name">LUMEN FOUNDATION</div>
    </header>

    <h1 class="headline">
      <span class="headline__main">SOCIAL</span>
      <span class="headline__sub">ENTERPRISE</span>
    </h1>

    <svg class="footer-band" viewBox="0 0 945 90" preserveAspectRatio="none" aria-hidden="true">
      <polygon points="0,8 470,8 490,17 0,17" fill="var(--band-dark)"/>
      <rect x="0" y="17" width="945" height="60" fill="var(--brand-green)"/>
      <polygon points="470,77 945,77 945,87 490,87" fill="var(--band-dark)"/>
    </svg>
    <div class="footer-band__url">www.lumenfoundation.sg</div>
  </main>
</body>
</html>
```